Copperfield Hide Renewal Product Label

We need a design for a label to be used on bottles of leather cleaner and conditioner products that will be used in curated kits. We would like it to incorporate our business logo as well as have an area that we can fill in later with the appropriate product name as needed. We would like to see designs that use shades of brown, but we are open to other colors often seen in leather. I am including the Copperfield Hide business Logo below, however again we would prefer to have the label in various shades of browns, rather than the red and grey, more like the mock-up that I am also attaching.

*** I am attaching examples of the types of bottles that will be used. They vary in size from 8 oz to 16 oz. if you are designing a label for a spray bottle they are from 16-32 oz. ***

```html
<!DOCTYPE html>
<html lang="en">
<head>
<meta charset="utf-8">
<title>Copperfield Hide Renewal – Leather Cleaner / Conditioner Labels</title>
<link rel="stylesheet" href="https://fonts.googleapis.com/css2?family=Montserrat:wght@500;800&family=Oswald:wght@500&display=swap">
<style>
  :root {
    --canvas: #ffffff;
    --hide-dark: #4a200c;
    --hide-mid: #7a3a14;
    --hide-light: #b9651f;
    --hide-glow: #d08333;
    --ink-light: #ffffff;
    --band: #f9c6b2;
    --band-ink: #e0603a;
    --cream: #f6e7d6;
    --ring: #3a170a;
  }
  * { box-sizing: border-box; margin: 0; padding: 0; }
  html, body {
    width: 1200px; height: 1200px; overflow: hidden;
    background: var(--canvas);
    font-family: "Montserrat", sans-serif;
  }
  .label-set { position: relative; width: 1200px; height: 1200px; }

  .label {
    position: absolute; overflow: hidden;
    color: var(--ink-light);
  }
  .label--spray {
    left: 90px; top: 210px; width: 560px; height: 780px;
    border-radius: 220px 220px 60px 60px;
  }
  .label--bottle {
    left: 740px; top: 250px; width: 380px; height: 700px;
    border-radius: 18px;
  }
  .label__hide {
    position: absolute; inset: 0;
    background:
      radial-gradient(ellipse 75% 60% at 85% 20%, var(--hide-glow) 0%, rgba(185,101,31,0.55) 45%, rgba(185,101,31,0) 80%),
      linear-gradient(165deg, var(--hide-mid) 0%, var(--hide-dark) 60%, var(--hide-mid) 100%);
  }

  .brand {
    position: absolute; display: flex; flex-direction: column; align-items: center;
  }
  .brand__dot {
    border-radius: 50%; background: var(--cream);
    border: 10px solid var(--ring);
  }
  .brand__name {
    margin-top: 12px; font-weight: 500; color: var(--ink-light);
    text-align: center; line-height: 1.15; letter-spacing: 0.03em;
  }
  .label--spray .brand { left: 300px; top: 70px; width: 220px; }
  .label--spray .brand__dot { width: 110px; height: 110px; }
  .label--spray .brand__name { font-size: 22px; }
  .label--bottle .brand { left: 190px; top: 60px; width: 170px; }
  .label--bottle .brand__dot { width: 84px; height: 84px; border-width: 8px; }
  .label--bottle .brand__name { font-size: 17px; }

  .title {
    position: absolute; left: 0; right: 0; text-align: center;
    font-weight: 800; letter-spacing: -0.01em; line-height: 1;
    text-shadow: 0 3px 6px rgba(0,0,0,0.45);
  }
  .label--spray .title { top: 330px; font-size: 82px; }
  .label--bottle .title { top: 290px; font-size: 62px; }

  .product-band {
    position: absolute; left: 50%; transform: translateX(-50%);
    background: var(--band); color: var(--band-ink);
    font-family: "Oswald", sans-serif; font-weight: 500;
    white-space: nowrap; line-height: 1;
  }
  .label--spray .product-band { top: 430px; font-size: 34px; padding: 6px 16px; }
  .label--bottle .product-band { top: 368px; font-size: 27px; padding: 5px 12px; }

  .benefits {
    position: absolute; border-left: 2px solid var(--band);
    list-style: none; line-height: 1.3;
  }
  .label--spray .benefits { left: 120px; top: 520px; padding: 4px 0 14px 12px; font-size: 20px; }
  .label--bottle .benefits { left: 30px; top: 460px; padding: 4px 0 10px 10px; font-size: 17px; }
  .benefits__icon { display: block; margin-top: 10px; }

  .volume {
    position: absolute; left: 0; right: 0; text-align: center;
    font-weight: 800; color: var(--cream);
  }
  .label--spray .volume { bottom: 70px; font-size: 22px; }
  .label--bottle .volume { bottom: 80px; font-size: 19px; }
</style>
</head>
<body>
<main class="label-set">

  <section class="label label--spray">
    <div class="label__hide" role="img" aria-label="Leather-grain background with decorative swirl in warm browns"></div>
    <div class="brand">
      <span class="brand__dot"></span>
      <span class="brand__name">Copperfield Hide Renewal</span>
    </div>
    <h1 class="title">LEATHER</h1>
    <p class="product-band">CLEANER / CONDITIONER</p>
    <ul class="benefits">
      <li>Protects against drying</li>
      <li>Replenishes</li>
      <li>Cleans</li>
      <li>
        <svg class="benefits__icon" width="40" height="40" viewBox="0 0 40 40" aria-hidden="true">
          <path d="M20 4 L23 17 L36 20 L23 23 L20 36 L17 23 L4 20 L17 17 Z" fill="none" stroke="var(--cream)" stroke-width="2"/>
        </svg>
      </li>
    </ul>
    <p class="volume">32 fl oz.</p>
  </section>

  <section class="label label--bottle">
    <div class="label__hide" role="img" aria-label="Leather-grain background with decorative swirl in warm browns"></div>
    <div class="brand">
      <span class="brand__dot"></span>
      <span class="brand__name">Copperfield Hide Renewal</span>
    </div>
    <h2 class="title">LEATHER</h2>
    <p class="product-band">CLEANER / CONDITIONER</p>
    <ul class="benefits">
      <li>Protects against drying</li>
      <li>Replenishes</li>
      <li>Cleans</li>
      <li>
        <svg class="benefits__icon" width="32" height="32" viewBox="0 0 40 40" aria-hidden="true">
          <path d="M20 4 L23 17 L36 20 L23 23 L20 36 L17 23 L4 20 L17 17 Z" fill="none" stroke="var(--cream)" stroke-width="2"/>
        </svg>
      </li>
    </ul>
    <p class="volume">16 fl oz.</p>
  </section>

</main>
</body>
</html>
```